Company Profile
Corvane Logistics Sdn Bhd is a well established and experienced freight forwarder in Kuala Lumpur, Malaysia. We specialize in air and sea forwarding, Custom Brokerage and regulatory compliance services, inland transportation,
overseas freighting and warehousing and distribution management. With our dedicated qualified and experienced professionals, we are fully committed to serving our clients.

Our Mission
Based on the motto “Quick, Reliable and Polite”, Corvane Logistics is dedicated to upholding the following three points corporate philosophy:
1. Adhering to the principle that “the customer always comes first”.
2. Contributing to the development of the local community.
3. Making it our duty to be responsible and sincere.

Our Edge
• One-Stop Logistics Solutions
• Extensive Network Throughout Malaysia
• Highly Qualified and Experienced Pool of Professionals
• Comprehensive IT Solutions
• Innovative and Customer-focused Solutions
• Flexible and Consistent in Managing Exceptions
• Total Supply Chain Visibility

Target Market(s)

We sell the logistics services to all the industry in Malaysia. (ONE Stop Logistics Solutions)

Industry/Entity Type

Logistic

Contact Information for Business Card

I want the back of the card to be white with the logo and slogan. i would like to see the logo on the front with the general info.

Requirements
Must have
• Name, Title, Office, Cell, Fax, Email, Address, Website
Nice to have
• Modern Design Business Card

```html
<!DOCTYPE html>
<html lang="en">
<head>
<meta charset="utf-8">
<title>Corvane Logistics – Business Card</title>
<link href="https://fonts.googleapis.com/css2?family=Source+Sans+3:wght@300;400;600;700&display=swap" rel="stylesheet">
<style>
  :root {
    --bg: #eceef0;
    --paper: #ffffff;
    --blue: #29a8dc;
    --blue-light: #6cc4ea;
    --blue-deep: #1d8fc4;
    --grey-band: #55595d;
    --ink: #5f6266;
    --ink-dark: #3f4245;
    --white: #ffffff;
  }
  * { margin: 0; padding: 0; box-sizing: border-box; }
  html, body {
    width: 1200px; height: 1200px; overflow: hidden;
    background: var(--bg);
    font-family: "Source Sans 3", sans-serif;
    color: var(--ink);
  }
  .brand-header {
    position: absolute; top: 40px; left: 0; width: 1200px;
    display: flex; justify-content: center; align-items: center; gap: 12px;
  }
  .brand-name { font-size: 34px; font-weight: 600; color: var(--ink); letter-spacing: 0.5px; white-space: nowrap; }
  .brand-dot { width: 16px; height: 16px; border-radius: 50%; background: var(--blue); flex: none; }

  .card {
    position: absolute; left: 220px; width: 760px; height: 434px;
    background: var(--paper); border-radius: 14px; overflow: hidden;
    box-shadow: 0 2px 0 #d6d8da, 0 4px 0 var(--blue-deep), 0 14px 30px rgba(0,0,0,0.15);
  }
  .card--back { top: 120px; }
  .card--front { top: 600px; }
  .card__bands { position: absolute; inset: 0; }
  .card__logo { position: absolute; display: flex; align-items: center; gap: 10px; }
  .card__logo .brand-name { font-size: 40px; }
  .card__logo .brand-dot { width: 18px; height: 18px; }
  .card--back .card__logo { left: 60px; top: 100px; }
  .card--front .card__logo { left: 44px; top: 226px; }
  .card--front .card__logo .brand-name { font-size: 36px; }

  .services {
    position: absolute; left: 120px; top: 300px; width: 530px;
    transform: rotate(-17.5deg); transform-origin: left top;
    color: var(--white); white-space: nowrap;
  }
  .services__title { font-size: 17px; font-weight: 600; letter-spacing: 0.5px; line-height: 1.2; }
  .services__rule { width: 170px; height: 1px; background: var(--white); margin: 5px 0 6px; }
  .services__list { font-size: 13px; line-height: 1.55; font-weight: 400; }
  .slogan {
    position: absolute; left: 430px; top: 374px;
    transform: rotate(-17.5deg); transform-origin: left top;
    color: var(--white); font-size: 15px; font-weight: 700; letter-spacing: 0.4px; white-space: nowrap;
  }

  .contact { position: absolute; left: 420px; top: 58px; }
  .contact__name { font-size: 22px; font-weight: 600; color: var(--ink-dark); letter-spacing: 0.5px; }
  .contact__title { font-size: 17px; font-weight: 300; color: var(--ink); margin-bottom: 14px; }
  .contact__row { display: flex; align-items: center; gap: 8px; font-size: 15px; line-height: 1.65; color: var(--ink-dark); }
  .contact__row--gap { margin-top: 10px; }
  .icon { width: 14px; height: 14px; border-radius: 2px; background: var(--blue); flex: none; }
  .icon svg { display: block; width: 14px; height: 14px; }
  .accent { color: var(--blue); font-weight: 600; }

  .company { position: absolute; right: 30px; bottom: 26px; text-align: right; color: var(--white); }
  .company__name { font-size: 19px; font-weight: 700; letter-spacing: 0.3px; }
  .company__address { font-size: 12px; font-weight: 400; margin-top: 4px; }
</style>
</head>
<body>

<header class="brand-header">
  <span class="brand-dot"></span>
  <span class="brand-name">Corvane Logistics</span>
</header>

<!-- Back of card: brand, services, slogan -->
<section class="card card--back">
  <svg class="card__bands" viewBox="0 0 760 434" aria-hidden="true">
    <path d="M0,330 L760,90 L760,434 L0,434 Z" fill="var(--blue)"/>
    <path d="M0,330 L760,90 L760,104 L0,344 Z" fill="var(--blue-light)" opacity="0.5"/>
    <path d="M168,434 L760,247 L760,434 Z" fill="var(--grey-band)"/>
  </svg>
  <div class="card__logo">
    <span class="brand-dot"></span>
    <span class="brand-name">Corvane Logistics</span>
  </div>
  <div class="services">
    <div class="services__title">WE'RE SPECIALIZE IN</div>
    <div class="services__rule"></div>
    <div class="services__list">
      • International Shipping (Air / Sea) • Transportation / Haulage • Consolidation – NVOCC<br>
      • Warehousing • Project Management • Packing • Supply Chain Management • Marine Insurance<br>
      • Tax Exemption Consultancy • Distribution • Custom Brokerage • Door to Door
    </div>
  </div>
  <div class="slogan">ONE STOP LOGISTICS SOLUTIONS</div>
</section>

<!-- Front of card: brand and contact details -->
<section class="card card--front">
  <svg class="card__bands" viewBox="0 0 760 434" aria-hidden="true">
    <path d="M0,434 L0,420 Q420,360 760,200 L760,434 Z" fill="var(--blue)"/>
    <path d="M0,420 Q420,360 760,200 L760,240 Q430,390 0,434 Z" fill="var(--blue-light)" opacity="0.45"/>
  </svg>
  <div class="card__logo">
    <span class="brand-dot"></span>
    <span class="brand-name">Corvane Logistics</span>
  </div>
  <div class="contact">
    <div class="contact__name">HAFIZUDDIN RAZAK</div>
    <div class="contact__title">Managing Director</div>
    <div class="contact__row">
      <span class="icon"><svg viewBox="0 0 14 14"><rect x="4.5" y="2.5" width="5" height="9" rx="1" fill="none" stroke="#fff" stroke-width="1.2"/></svg></span>
      + 6012-480 7315
    </div>
    <div class="contact__row">
      <span class="icon"><svg viewBox="0 0 14 14"><path d="M4 3 L6 3 L6.5 5.5 L5.3 6.3 Q6.3 8.3 7.8 8.8 L8.6 7.6 L11 8.2 L11 10.2 Q6 10.8 3.8 5 Z" fill="#fff"/></svg></span>
      + (603) 5521 3806 / 3807
    </div>
    <div class="contact__row">
      <span class="icon"><svg viewBox="0 0 14 14"><rect x="3" y="6" width="8" height="5" fill="none" stroke="#fff" stroke-width="1.2"/><rect x="4.5" y="3" width="5" height="3" fill="#fff"/></svg></span>
      + (603) 5521 3809
    </div>
    <div class="contact__row contact__row--gap">
      <span class="icon"><svg viewBox="0 0 14 14"><rect x="3" y="4" width="8" height="6" fill="none" stroke="#fff" stroke-width="1.2"/><path d="M3 4 L7 7.5 L11 4" fill="none" stroke="#fff" stroke-width="1.2"/></svg></span>
      <span>hafiz.razak@<span class="accent">corvane</span>.com.my</span>
    </div>
    <div class="contact__row">
      <span class="icon"><svg viewBox="0 0 14 14"><circle cx="7" cy="7" r="4" fill="none" stroke="#fff" stroke-width="1.1"/><path d="M3 7 H11 M7 3 V11" stroke="#fff" stroke-width="1"/></svg></span>
      <span>www.<span class="accent">corvane</span>.com.my</span>
    </div>
  </div>
  <div class="company">
    <div class="company__name">CORVANE LOGISTICS SDN. BHD. (1204736-K)</div>
    <div class="company__address">No. 8B, 2nd Floor, Jalan Sentosa 3C, Taman Sentosa Perdana, 41200 Klang, Selangor Darul Ehsan, Malaysia</div>
  </div>
</section>

</body>
</html>
```